依頼詳細
拠点周辺での新規顧客の獲得及び新拠点の営業開始の為、新聞折込を計画しており、新聞折込用のチラシ製作をお願い致します。お手入れできていないお庭をなんとかしたい!と思っている方、ご自分でお手入れしているもののやはりプロに頼みたい!と思っている方の目に留まるデザインを希望しております。ご相談を受け、現地で状態をしっかり確認した後ご提案、お見積りさせて頂く為、価格や料金プランはございません。また、新拠点の営業期間は当面3月〜5月の予定です。
記載項目
社  名:樋口庭苑
営業拠点:長野本店、茅野新店※3月〜5月
受付時間:9:30〜18:30 ※年中無休
電話番号:026-318-4452
(携帯 :090-7723-6041)
E- m a i l:info@hgchteien-example.com
本店住所:長野市若葉台西2丁目4-7 コーポ白樺105
サイズ
A4
ページ数
片面
希望イメージ
シンプル 複雑
単色 カラフル
暗い 明るい
日常 高級
遊び心 厳粛
未来的 伝統的
女性的 男性的
希望する色
緑系、水色系
納品ファイル
• 高解像度JPG (.jpg)
補足説明
◾️依頼タイトル変更
◾️施工例などの写真は使用しません。
一目で『業者のチラシ』と分かるものとは一線を画し、
「これ植木屋さん?!」と意表を突くデザイン性に富んだチラシを求めております。
抽象的で申し訳ないのですが、お力添えをお願い致します。

◾️記載項目の事業者情報の他、下記の記載をお願い致します。
・グリーンアドバイザーがお庭をなんとかしたい方のお悩みに丁寧にお応えする、という趣旨
・ご相談、お見積りは無料であること
・茅野市(長野県)で営業を開始すること※営業期間は3月から5月
◾️他社様ですが、素人なりに製作した過去のサンプルを添付しました。
*誠に申し訳ございませんが、
『概要・特徴』の内容を誤っておりました。
1級技能士と記載しておりますが、
造園関連ではございませんでした。
本当に申し訳ございません。
ご迷惑をおかけいたしますが、
記載項目からは外していただきますよう、
何卒お願い申し上げます。
■新聞折込は長野市内の部数を多めに予定しておりますので、
茅野新店についての記載は目立つ配置でなくて良いです。
*ご提案いただける方の制限につきまして、
訂正させていただいております。
多くの皆様のご提案をお待ちしております!
*前回同様
■ 選んだ理由

これ、植木屋さんなんだー!と驚くなんとも清潔感のある斬新さと、読みやすく分かりやすいシンプルさがとても印象的で、この度選ばせて頂きました。

■ 提案者全員のお礼・コメント

この度は、当方のご依頼にこのように多くの皆様にご提案をいただき、ただただ感謝申し上げます。利用させていただくのが初めてで、ご説明不足や当方の不手際等で大変お手数をおかけしてしまったにも関わらず、皆様のご対応の迅速さに、脱帽でした。本当に、有難うございました。

```html
<!DOCTYPE html>
<html lang="ja">
<head>
<meta charset="utf-8">
<title>樋口庭苑 グリーンアドバイザー チラシ</title>
<link rel="stylesheet" href="https://fonts.googleapis.com/css2?family=M+PLUS+Rounded+1c:wght@400;500;700;800&display=swap">
<style>
  :root{
    --paper:#f6f9f1;
    --green:#6cb02c;
    --green-dark:#3f7d1e;
    --leaf:#a9cf7a;
    --leaf-pale:#e3efd3;
    --sky:#cfeaf4;
    --sky-text:#3d8fb8;
    --tag:#f3dc7a;
    --ink:#2f3a2a;
    --footer:#e6f0d9;
  }
  *{box-sizing:border-box;margin:0;padding:0}
  html,body{width:854px;height:1200px;overflow:hidden}
  body{background:var(--paper);font-family:"M PLUS Rounded 1c",sans-serif;color:var(--ink);position:relative}

  .tagline{position:absolute;top:70px;left:0;width:100%;text-align:center;font-size:21px;font-weight:500;color:var(--green-dark);letter-spacing:.02em}

  .hero-art{position:absolute;left:90px;top:130px;width:610px;height:400px;border-radius:40% 50% 45% 40%;
    background:radial-gradient(ellipse at 45% 50%,#8fc25a 0%,#b9dc93 45%,rgba(246,249,241,0) 75%)}

  .free-badge{position:absolute;left:592px;top:160px;width:140px;height:140px;border-radius:50%;background:var(--sky);
    display:flex;align-items:center;justify-content:center;text-align:center;color:var(--sky-text);font-weight:800;font-size:25px;line-height:1.3}

  .headline{position:absolute;top:545px;left:0;width:100%;text-align:center;color:var(--green);font-weight:800;font-size:54px;line-height:1.3;letter-spacing:.01em}

  .worries{position:absolute;top:690px;left:80px;width:694px;display:flex;justify-content:space-between}
  .worry{width:150px;text-align:center}
  .worry-icon{width:114px;height:114px;margin:0 auto;border-radius:50%;background:var(--leaf-pale);position:relative}
  .worry-icon span{position:absolute;left:50%;top:50%;width:46px;height:64px;transform:translate(-50%,-55%);border-radius:50% 50% 40% 40%;background:var(--leaf)}
  .worry-icon.conifer span{border-radius:50% 50% 10% 10%;background:#7fb04a}
  .worry-text{margin-top:14px;font-size:15px;font-weight:500;line-height:1.45;color:var(--ink)}

  .services{position:absolute;top:912px;left:50px;width:754px;display:flex;justify-content:space-between}
  .service{background:var(--tag);padding:6px 10px;font-size:19px;font-weight:700;color:var(--ink)}

  .footer{position:absolute;left:0;top:975px;width:100%;height:225px;background:var(--footer)}
  .footer-lead{position:absolute;left:90px;top:32px;font-size:15px;font-weight:700;line-height:1.4;text-align:center}
  .brand{position:absolute;left:262px;top:20px;font-size:58px;font-weight:800;color:var(--green-dark);letter-spacing:.06em}
  .branches{position:absolute;left:550px;top:22px;font-size:27px;font-weight:800;color:var(--green-dark);line-height:1.3}
  .branches small{font-size:12px;font-weight:700;margin-left:4px;vertical-align:middle}
  .address{position:absolute;left:90px;top:105px;font-size:13px;font-weight:500}
  .contact{position:absolute;left:50px;top:128px;width:754px;display:flex;align-items:center;gap:28px;font-size:26px;font-weight:800;color:var(--ink)}
  .contact-item{display:flex;align-items:center;gap:6px}
  .contact-item.mail{font-size:17px}
  .contact svg{width:26px;height:26px;fill:var(--green-dark)}
  .bottom-band{position:absolute;left:0;bottom:0;width:100%;height:22px;background:var(--green)}
</style>
</head>
<body>
  <p class="tagline">一本一本の庭木の状態を丁寧に確認し、適切なご提案・お見積りをします。</p>

  <div class="hero-art" role="img" aria-label="緑のマントを着て空を飛ぶ剪定ばさみを持ったヒーローと小鳥のイラスト"></div>

  <div class="free-badge">ご相談・<br>お見積り<br>無料</div>

  <h1 class="headline">グリーンアドバイザーが<br>庭木1本から承ります!</h1>

  <ul class="worries">
    <li class="worry"><div class="worry-icon" role="img" aria-label="丸い庭木のアイコン"><span></span></div><p class="worry-text">家の前庭の雑草を<br>なんとかしたい!</p></li>
    <li class="worry"><div class="worry-icon conifer" role="img" aria-label="針葉樹のアイコン"><span></span></div><p class="worry-text">草木の手入れの<br>仕方がわからない</p></li>
    <li class="worry"><div class="worry-icon" role="img" aria-label="広葉樹のアイコン"><span></span></div><p class="worry-text">庭木のあれこれ<br>相談したい</p></li>
    <li class="worry"><div class="worry-icon conifer" role="img" aria-label="針葉樹のアイコン"><span></span></div><p class="worry-text">やはり庭はプロに<br>整えてもらいたい!</p></li>
  </ul>

  <ul class="services">
    <li class="service">庭木手入れ</li>
    <li class="service">草刈り</li>
    <li class="service">害虫駆除</li>
    <li class="service">消毒</li>
    <li class="service">芝張り芝刈り</li>
    <li class="service">樹木の伐採</li>
    <li class="service">伐根</li>
  </ul>

  <footer class="footer">
    <p class="footer-lead">お庭・緑に関する<br>ご要望ご相談は</p>
    <p class="brand">樋口庭苑</p>
    <p class="branches">長野本店<br>茅野新店<small>3月〜5月</small></p>
    <p class="address">長野市若葉台西2丁目4-7 コーポ白樺105 ［受付時間］9:30〜18:30 ■年中無休</p>
    <div class="contact">
      <span class="contact-item"><svg viewBox="0 0 24 24"><path d="M6.6 10.8a15.1 15.1 0 0 0 6.6 6.6l2.2-2.2a1 1 0 0 1 1-.25 11.4 11.4 0 0 0 3.6.57 1 1 0 0 1 1 1V20a1 1 0 0 1-1 1A17 17 0 0 1 3 4a1 1 0 0 1 1-1h3.5a1 1 0 0 1 1 1c0 1.25.2 2.45.57 3.57a1 1 0 0 1-.25 1z"/></svg>026-318-4452</span>
      <span class="contact-item"><svg viewBox="0 0 24 24"><path d="M7 1h10a2 2 0 0 1 2 2v18a2 2 0 0 1-2 2H7a2 2 0 0 1-2-2V3a2 2 0 0 1 2-2zm0 3v14h10V4zm5 15.5a1 1 0 1 0 0 2 1 1 0 0 0 0-2z"/></svg>090-7723-6041</span>
      <span class="contact-item mail"><svg viewBox="0 0 24 24"><path d="M3 5h18a1 1 0 0 1 1 1v12a1 1 0 0 1-1 1H3a1 1 0 0 1-1-1V6a1 1 0 0 1 1-1zm1 2.3V17h16V7.3l-8 5.2z M4.5 7 12 11.8 19.5 7z"/></svg>info@hgchteien-example.com</span>
    </div>
    <div class="bottom-band"></div>
  </footer>
</body>
</html>
```